Company or website name
- The Quillstone Movers and Storage
- Links to the website
- Quillstonehauling.com
- Describe your company and organization and target audience
- Residential and commercial moving and relocation service that needs a website redesign.
- The design should have the following
- I NEED THE WEBSITE TO BE SIMPLE AND STRAIGHT TO THE POINT...MAIN CONCERN IS THAT THEY FILL OUT INFORMATION TO GET QUOTE. SITE EXAMPLE THAT I LIKE IS ( WWW.MYPELDRAN.COM) https://www.orvikhaulage.com/

```html
<!DOCTYPE html>
<html lang="en">
<head>
<meta charset="utf-8">
<title>Quillstone Movers and Storage</title>
<link href="https://fonts.googleapis.com/css2?family=Montserrat:wght@400;500;600;700&display=swap" rel="stylesheet">
<style>
:root{
  --red:#f40000;
  --ink:#111111;
  --muted:#8a8a8a;
  --field:#ececec;
  --soft:#f4f4f4;
  --line:#d6d6d6;
  --white:#ffffff;
  --gold:#f5b400;
}
*{box-sizing:border-box;margin:0;padding:0}
html,body{width:1200px;height:3738px;overflow:hidden}
body{position:relative;font-family:"Montserrat",sans-serif;color:var(--ink);background:var(--white)}
.abs{position:absolute}
.header{left:0;top:0;width:1200px;height:97px;background:var(--white)}
.brand{display:flex;align-items:center;gap:10px;font-weight:700;color:var(--ink)}
.brand .dot{width:26px;height:26px;background:var(--ink)}
.header .brand{left:87px;top:30px;font-size:28px;letter-spacing:1px}
.nav{top:38px;font-size:15px;font-weight:500}
.caret{display:inline-block;width:7px;height:7px;border-right:2px solid var(--ink);border-bottom:2px solid var(--ink);transform:rotate(45deg);margin:0 0 3px 8px}
.btn{display:flex;align-items:center;justify-content:center;font-weight:600;border-radius:3px}
.btn-red{background:var(--red);color:var(--white)}
.hero{left:0;top:97px;width:1200px;height:617px;background:linear-gradient(180deg,#c9909f 0%,#b77b87 55%,#94636b 100%)}
.hero-title{left:0;width:1200px;top:262px;text-align:center;color:var(--white);font-size:46px;font-weight:700}
.hero-sub{left:0;width:1200px;top:323px;text-align:center;color:var(--white);font-size:15px}
.gray-band{left:0;top:714px;width:1200px;height:911px;background:var(--soft)}
.quote-card{left:203px;top:406px;width:794px;height:552px;background:var(--white);border-radius:8px;box-shadow:0 2px 10px rgba(0,0,0,.12)}
.quote-title{left:0;width:100%;top:36px;text-align:center;font-size:20px;font-weight:700}
.tab{top:74px;width:94px;height:93px;background:#efefef;border-radius:3px;box-shadow:0 1px 4px rgba(0,0,0,.15);display:flex;flex-direction:column;align-items:center;justify-content:center;gap:8px;font-size:11px;color:#888}
.tab.active{background:var(--red);color:var(--white)}
.label{font-size:15px;font-weight:500}
.field{width:230px;height:38px;background:var(--field);color:#b5b5b5;font-size:15px;padding:10px 12px;white-space:nowrap}
.btn-outline{border:1px solid #999;color:var(--ink);background:var(--white)}
.section-title{left:0;width:1200px;text-align:center;font-size:38px;font-weight:700}
.svc{top:1129px;width:231px;height:399px;background:var(--white);box-shadow:0 1px 5px rgba(0,0,0,.1);text-align:center}
.svc svg{margin-top:46px}
.svc h3{font-size:27px;font-weight:700;margin-top:20px;line-height:34px}
.svc p{font-size:15px;line-height:22px;color:var(--muted);padding:0 14px;margin-top:14px}
.svc .more{position:absolute;left:0;width:100%;top:362px;color:var(--red);font-size:15px;font-weight:600}
.svc.featured{background:var(--red);color:var(--white)}
.svc.featured p,.svc.featured .more{color:var(--white)}
.lead{left:0;width:1200px;text-align:center;font-size:21px;line-height:31px}
.photo{background:linear-gradient(180deg,#5f7a47 0%,#dfe2e0 35%,#cfd2d0 60%,#4f7a2e 75%,#3f6b24 100%)}
.about{left:663px;top:1960px;width:420px;display:flex;flex-direction:column;align-items:flex-start}
.about h2{font-size:40px;font-weight:700;line-height:50px}
.about p{margin-top:8px;font-size:14.5px;line-height:22px;color:#333}
.about .btn{margin-top:18px;width:150px;height:36px;font-size:15px}
.testi{top:2556px;width:460px;font-size:15px;line-height:22px;color:#333}
.avatar{width:60px;height:60px;border-radius:50%;background:radial-gradient(circle,#6a5a4e,#2c2622)}
.person{font-size:17px;font-weight:600}
.stars{color:var(--gold);font-size:14px;letter-spacing:2px}
.arrow{top:2600px;width:18px;height:18px;border-left:3px solid #bbb;border-bottom:3px solid #bbb}
.cta{left:87px;top:2895px;width:1026px;height:239px;border-radius:6px;background:linear-gradient(90deg,#c98a92 0%,#8f4a52 45%,#7a3a42 100%);color:var(--white);text-align:center}
.cta h2{font-size:43px;font-weight:700;margin-top:42px}
.cta p{font-size:16px;line-height:22px;margin-top:8px}
.footer{left:0;top:3240px;width:1200px;height:498px;background:var(--soft)}
.footer .brand{left:130px;top:115px;font-size:30px}
.foot-text{left:116px;top:195px;width:300px;font-size:14px;line-height:25px;color:#666}
.social{top:301px;width:22px;height:22px;border-radius:50%;background:var(--ink)}
.col{top:152px;font-size:14.5px;color:#666;line-height:38px}
.col h4{font-size:18px;font-weight:600;color:var(--ink);line-height:22px;margin-bottom:12px}
.rule{left:0;top:441px;width:1200px;height:1px;background:var(--line)}
.copy{left:0;top:463px;width:1200px;text-align:center;font-size:13px;color:#666}
</style>
</head>
<body>

<header class="abs header">
  <div class="abs brand"><span class="dot"></span>Quillstone</div>
  <div class="abs nav" style="left:379px">About</div>
  <div class="abs nav" style="left:476px">Moving Services<span class="caret"></span></div>
  <div class="abs nav" style="left:669px">Resources<span class="caret"></span></div>
  <div class="abs nav" style="left:817px">Contacts</div>
  <div class="abs btn btn-red" style="left:963px;top:29px;width:150px;height:38px;font-size:13px">Request a Quote</div>
</header>

<section class="abs hero" role="img" aria-label="Moving truck parked under a cloudy sky, tinted red"></section>
<h1 class="abs hero-title">We Help Move Lives Forward</h1>
<p class="abs hero-sub">Providing Local, Long Distance Residential and Commercial Moving Services Since 2006</p>

<div class="abs gray-band"></div>

<form class="abs quote-card">
  <h2 class="abs quote-title">GET A FREE MOVING QUOTE!</h2>
  <div class="abs tab active" style="left:189px">
    <svg width="40" height="38" viewBox="0 0 40 38"><path d="M6 20 L20 8 L34 20 V36 H6Z" fill="#fff"/><rect x="16" y="26" width="8" height="10" fill="#f40000"/><circle cx="33" cy="8" r="5" fill="#fff"/></svg>
    Residential</div>
  <div class="abs tab" style="left:296px">
    <svg width="40" height="38" viewBox="0 0 40 38"><path d="M4 14 L20 4 L36 14 V36 H4Z" fill="#777"/><circle cx="14" cy="20" r="4" fill="#efefef"/><circle cx="26" cy="20" r="4" fill="#efefef"/></svg>
    Senior</div>
  <div class="abs tab" style="left:404px">
    <svg width="40" height="38" viewBox="0 0 40 38"><rect x="4" y="4" width="32" height="32" fill="#777"/><rect x="9" y="10" width="22" height="5" fill="#efefef"/><rect x="9" y="22" width="8" height="14" fill="#efefef"/><rect x="22" y="22" width="9" height="6" fill="#efefef"/></svg>
    Commercial</div>
  <div class="abs tab" style="left:512px">
    <svg width="40" height="38" viewBox="0 0 40 38"><path d="M4 10 L20 3 L36 10 V36 H4Z" fill="#777"/><rect x="10" y="16" width="20" height="20" fill="#efefef"/><path d="M10 22H30M10 28H30" stroke="#777" stroke-width="2"/></svg>
    Storage</div>

  <label class="abs label" style="left:151px;top:203px">I am moving from . . .</label>
  <div class="abs field" style="left:151px;top:230px">Zip Code</div>
  <label class="abs label" style="left:414px;top:203px">I am moving to . . .</label>
  <div class="abs field" style="left:414px;top:230px">Zip Code</div>
  <label class="abs label" style="left:151px;top:282px">Moving Date</label>
  <div class="abs field" style="left:151px;top:308px">02 / 31 / 2022</div>
  <label class="abs label" style="left:414px;top:282px">Full Name</label>
  <div class="abs field" style="left:414px;top:308px">Mara Velde</div>
  <label class="abs label" style="left:151px;top:360px">E-Mail Address</label>
  <div class="abs field" style="left:151px;top:386px">mail@quillstone.com</div>
  <label class="abs label" style="left:414px;top:360px">Phone Number</label>
  <div class="abs field" style="left:414px;top:386px">(+000) 000 0000</div>
  <div class="abs btn btn-red" style="left:208px;top:452px;width:172px;height:48px;font-size:17px">Free Quote</div>
  <div class="abs btn btn-outline" style="left:414px;top:452px;width:171px;height:48px;font-size:17px">Contact Us</div>
</form>

<h2 class="abs section-title" style="top:1045px">Moving Services</h2>

<article class="abs svc featured" style="left:87px">
  <svg width="100" height="98" viewBox="0 0 100 98"><circle cx="30" cy="40" r="22" fill="#fff"/><path d="M26 62 L58 36 L90 62 V96 H26Z" fill="#fff"/><rect x="44" y="72" width="12" height="24" fill="#f40000"/><rect x="64" y="72" width="16" height="12" fill="#f40000"/><circle cx="85" cy="14" r="10" fill="#fff"/></svg>
  <h3>Residential</h3>
  <p>We are the residential movers who strive to make your relocation experience simplified - regardless of whether you are moving...</p>
  <span class="more">Learn More</span>
</article>
<article class="abs svc" style="left:350px">
  <svg width="100" height="98" viewBox="0 0 100 98"><rect x="6" y="4" width="88" height="10" fill="#f40000"/><rect x="10" y="20" width="80" height="76" fill="#f40000"/><rect x="20" y="30" width="60" height="12" fill="#fff"/><rect x="20" y="54" width="28" height="14" fill="#fff"/><rect x="58" y="54" width="22" height="42" fill="#fff"/></svg>
  <h3>Commercial</h3>
  <p>As commercial movers, Quillstone Inc is one the industry leaders in providing the highest quality services at competitive...</p>
  <span class="more">Learn More</span>
</article>
<article class="abs svc" style="left:617px">
  <svg width="100" height="98" viewBox="0 0 100 98"><path d="M2 26 L50 0 L98 26 V98 H2Z" fill="#f40000"/><circle cx="32" cy="50" r="10" fill="#fff"/><circle cx="68" cy="50" r="10" fill="#fff"/><rect x="20" y="66" width="24" height="32" rx="8" fill="#fff"/><rect x="56" y="66" width="24" height="32" rx="8" fill="#fff"/></svg>
  <h3>Senior</h3>
  <p>Is the thought of moving as a senior too daunting for you? It can often times be a draining process. If you are concerned about...</p>
  <span class="more">Learn More</span>
</article>
<article class="abs svc" style="left:882px">
  <svg width="100" height="98" viewBox="0 0 100 98"><path d="M2 20 L50 0 L98 20 V98 H2Z" fill="#f40000"/><rect x="18" y="36" width="64" height="62" fill="#fff"/><path d="M18 52H82M18 68H82M18 84H82" stroke="#f40000" stroke-width="6"/></svg>
  <h3>Storage</h3>
  <p>Need to move your extra belongings into a storage facility? If you want a company to handle all your storage needs from A to Z..</p>
  <span class="more">Learn More</span>
</article>

<h2 class="abs section-title" style="top:1717px">Moving Families &amp; Businesses For Over A Decade</h2>
<p class="abs lead" style="top:1775px">As movers since 2007, Quillstone Inc has an expertise in transportation and storage services<br>that is unequaled by other moving companies.</p>

<div class="abs photo" style="left:87px;top:1918px;width:511px;height:395px" role="img" aria-label="White moving truck parked on a grassy lawn in front of trees"></div>
<div class="abs about">
  <h2>About Us</h2>
  <p>At Quillstone Inc we coordinate local, long distance moves that incorporate all the necessary moving services to est serve your individual move. In addition, we offer our commercial clients a wide array of specialized transportation services for high-value products. We are committed to safe, simple moving experiences for family, businesses and employees.</p>
  <div class="btn btn-red">Learn More</div>
</div>

<h2 class="abs section-title" style="top:2428px">What clients are saying</h2>
<div class="abs arrow" style="left:50px;transform:rotate(45deg)"></div>
<div class="abs arrow" style="left:1130px;transform:rotate(-135deg)"></div>
<p class="abs testi" style="left:119px">Great Service...Easy...Stress free move. Provided accurate move estimate. Professional staff all around. From Estimate to delivery. Professional and Friendly pick-up, Transportation, and Delivery. Thank You so Much.</p>
<div class="abs avatar" style="left:119px;top:2658px" role="img" aria-label="Customer portrait"></div>
<div class="abs person" style="left:196px;top:2667px">Darnell, San Antonio TX</div>
<div class="abs stars" style="left:196px;top:2690px">★★★★★</div>
<p class="abs testi" style="left:624px">Both the folks that packed up my belongings and the folks that delivered them were very efficient and professional. I was a little anxious about my antique furniture, but everything arrived in great shape.</p>
<div class="abs avatar" style="left:624px;top:2658px" role="img" aria-label="Customer portrait"></div>
<div class="abs person" style="left:701px;top:2667px">Rita K., Melbourne FL</div>
<div class="abs stars" style="left:701px;top:2690px">★★★★★</div>

<section class="abs cta" role="img" aria-label="Mover in a dark red shirt, tinted red background">
  <h2>Let's Get You A Free Quote</h2>
  <p>No matter the size or scope of your relocation, Quillstone Inc Moving can offer<br>you the simple and stress-free services you are looking for.</p>
  <div class="abs btn btn-red" style="left:419px;top:152px;width:188px;height:48px;font-size:17px">Free Quote Now</div>
</section>

<footer class="abs footer">
  <div class="abs brand"><span class="dot"></span>Quillstone</div>
  <p class="abs foot-text">Lorem ipsum, or lipsum as it is sometimes known, is dummy text used in laying out print, graphic or web designs. .</p>
  <span class="abs social" style="left:160px"></span>
  <span class="abs social" style="left:207px"></span>
  <span class="abs social" style="left:253px"></span>
  <span class="abs social" style="left:298px"></span>
  <div class="abs col" style="left:505px"><h4>Quick Links</h4>About<br>Moving Services<br>Resources<br>Contacts</div>
  <div class="abs col" style="left:725px"><h4>User Links</h4>Account<br>Get Quote<br>Message<br>Logout</div>
  <div class="abs col" style="left:914px"><h4>Information</h4>Privacy Policy<br>Terms &amp; Conditions</div>
  <div class="abs rule"></div>
  <p class="abs copy">Copyright © 2022 by Quillstone&nbsp; All rights reserved.</p>
</footer>

</body>
</html>
```